Corporate Powerpoint templates

I wish to have a standardized template for our manufacturing company. We manufacture baseball caps for major sport leagues and teams.
Our powerpoint should be clean, yet stylish.
We do a lot of presentations for technical trainings, KPI reports, quality assurance training.
We have factories in China, Bangladesh, and Mexico, so the look and feel must be internationally accepted.

Target Market(s)

Branded customers

Industry/Entity Type

Headwear Manufacturing

Font styles to use
Sans Serif

Colors
00AB8E
00BBA5
67D7C9
C6EFE9
E9F9F6

Requirements
Must have
• Spreadsheet slides, graphs, photographic reports
Nice to have
• Sporty, trendy, yet corporate feel.

```html
<!DOCTYPE html>
<html lang="en">
<head>
<meta charset="utf-8">
<title>Headwear Manufacturing – Presentation Template</title>
<link href="https://fonts.googleapis.com/css2?family=Montserrat:wght@400;500;600;700;800&display=swap" rel="stylesheet">
<style>
  :root {
    --green: #00ab8e;
    --green-2: #00bba5;
    --tab: #2fb99c;
    --mint: #67d7c9;
    --mint-soft: #c6efe9;
    --mint-pale: #e9f9f6;
    --beige: #f2e3cd;
    --sage: #c4d8bd;
    --ink: #262626;
    --body: #4a4a4a;
    --canvas: #8f8f8f;
    --soft-grey: #f2f1f1;
    --teal-bar: #4db6c5;
    --tan-bar: #c4ac72;
    --row-head: #9eaabb;
  }
  * { box-sizing: border-box; margin: 0; padding: 0; }
  html, body { width: 1200px; height: 3470px; overflow: hidden; }
  body {
    background: var(--canvas);
    font-family: "Montserrat", sans-serif;
    color: var(--body);
    position: relative;
  }
  .slide {
    position: absolute;
    left: 143px;
    width: 914px;
    height: 514px;
    overflow: hidden;
    background: #fff;
  }
  .slide-1 { top: 104px; background: var(--beige); }
  .slide-2 { top: 653px; }
  .slide-3 { top: 1203px; background: var(--soft-grey); }
  .slide-4 { top: 1752px; }
  .slide-5 { top: 2302px; }
  .slide-6 { top: 2851px; }

  .abs { position: absolute; }
  .title {
    position: absolute;
    font-weight: 800;
    font-size: 39px;
    line-height: 46px;
    color: var(--ink);
    letter-spacing: 0.5px;
  }
  .copy {
    position: absolute;
    font-size: 13.4px;
    line-height: 26.3px;
    color: var(--body);
    text-align: justify;
  }
  .copy p + p { margin-top: 26px; }

  .page-no {
    position: absolute;
    left: 865px;
    top: 467px;
    width: 34px;
    height: 34px;
    border-radius: 50%;
    background: var(--green);
    color: #fff;
    font-size: 12px;
    font-weight: 600;
    display: flex;
    align-items: center;
    justify-content: center;
  }
  .page-no.light { background: #fff; color: var(--green); }

  .brand-tab { position: absolute; right: 0; top: 0; width: 591px; height: 86px; }
  .brand-tab svg { position: absolute; inset: 0; }
  .brand-tab span {
    position: absolute;
    left: 380px;
    top: 9px;
    color: #fff;
    font-weight: 800;
    font-size: 17px;
    line-height: 20px;
  }

  .photo { position: absolute; }

  /* slide 1 */
  .s1-photo {
    left: 0; top: 94px; width: 459px; height: 325px;
    background: radial-gradient(ellipse at 45% 45%, #5a4032 0%, #2c211c 45%, #140f0d 100%);
  }
  .s1-product {
    left: 535px; top: 31px; width: 249px; height: 185px;
    background: radial-gradient(ellipse at 50% 50%, #3a3a3a 0%, #121212 55%, rgba(18,18,18,0) 72%);
  }
  .s1-title { left: 510px; top: 248px; font-size: 40px; line-height: 45px; }
  .s1-copy { left: 511px; top: 356px; width: 380px; font-size: 16.5px; line-height: 31px; text-align: left; }

  /* slide 2 */
  .s2-title { left: 43px; top: 46px; color: #fff; font-size: 39px; line-height: 47px; }
  .s2-photo {
    left: 43px; top: 183px; width: 415px; height: 267px;
    background: linear-gradient(120deg, #2a2522 0%, #4b3a30 40%, #7a4a35 75%, #2d2420 100%);
  }
  .s2-copy { left: 506px; top: 115px; width: 371px; }

  /* slide 3 */
  .s3-title { left: 43px; top: 46px; }
  .s3-copy { left: 46px; top: 124px; width: 369px; }
  .s3-chart { left: 490px; top: 211px; width: 377px; height: 190px; }

  /* slide 4 */
  .s4-title { left: 43px; top: 39px; }
  .s4-copy { left: 43px; top: 149px; width: 842px; font-size: 13px; }
  .qa-table {
    position: absolute;
    left: 43px; top: 284px;
    border-collapse: separate;
    border-spacing: 4px 6px;
    font-size: 8.5px;
    margin-left: -4px;
  }
  .qa-table th, .qa-table td { height: 29px; text-align: center; padding: 0 4px; white-space: nowrap; }
  .qa-table thead th { color: #fff; font-weight: 700; font-size: 7.5px; height: 22px; width: 78px; }
  .qa-table thead th.blank { background: none; width: 117px; }
  .qa-table tbody th {
    background: var(--row-head); color: #fff; font-weight: 600; font-size: 7.5px; text-align: left; padding-left: 12px; width: 117px;
  }
  .qa-table tbody td { color: #444; border-bottom: 2px solid #f0f2f6; }
  .qa-table tfoot th, .qa-table tfoot td {
    font-weight: 700; color: #222; border-top: 1px solid #6f7a8a; border-bottom: 1px solid #6f7a8a; height: 24px;
  }
  .qa-table tfoot th { text-align: left; padding-left: 12px; border-left: 1px solid #6f7a8a; font-size: 7.5px; }
  .qa-table tfoot td:last-child { border-right: 1px solid #6f7a8a; }
  .c-peri { background: #8fa5ee; }
  .c-teal { background: #4ec2c0; }
  .c-blue { background: #58b2e6; }
  .c-cyan { background: #55c6dd; }

  /* slide 5 */
  .s5-title { left: 43px; top: 34px; }
  .s5-copy { left: 43px; top: 88px; width: 842px; font-size: 13px; }
  .s5-dash {
    left: 43px; top: 158px; width: 755px; height: 339px;
    background: linear-gradient(135deg, #e4e8f2 0%, #eef1f7 50%, #dde3ef 100%);
  }

  /* slide 6 */
  .s6-photo {
    left: 0; top: 0; width: 914px; height: 514px;
    background: linear-gradient(180deg, #6f6478 0%, #a88a8a 22%, #c79c7c 36%, #8d7664 52%, #5b5a46 70%, #3c4a33 100%);
  }
  .s6-ring { left: 526px; top: 57px; width: 370px; height: 370px; border-radius: 50%; background: rgba(0,171,142,0.45); }
  .s6-disc { left: 545px; top: 76px; width: 332px; height: 332px; border-radius: 50%; background: var(--green); }
  .s6-text {
    position: absolute; left: 545px; top: 76px; width: 332px; height: 332px;
    color: #fff; text-align: center; font-weight: 800;
  }
  .s6-brand { position: absolute; top: 96px; width: 100%; font-size: 21px; line-height: 29px; }
  .s6-thanks { position: absolute; top: 162px; width: 100%; font-size: 42px; line-height: 48px; }
  .s6-contact { position: absolute; top: 230px; width: 100%; font-size: 16.5px; line-height: 24px; font-weight: 700; }
</style>
</head>
<body>

<!-- 01 Cover -->
<section class="slide slide-1">
  <svg class="abs" width="914" height="514" viewBox="0 0 914 514" aria-hidden="true">
    <circle cx="703" cy="-77" r="215" fill="var(--sage)"/>
    <path d="M0,0 H329 C470,95 488,420 369,514 H0 Z" fill="var(--green)"/>
  </svg>
  <div class="photo s1-photo" role="img" aria-label="Photo of a brown leather baseball helmet resting on a wooden bat"></div>
  <div class="photo s1-product" role="img" aria-label="Product photo of a glossy black batting helmet"></div>
  <h1 class="title s1-title">HEADWEAR<br>MANUFACTURING</h1>
  <p class="copy s1-copy">Sed ut perspiciatis unde omnis iste natus error sit voluptaaccusantium oloremquete irure dolor in reprehenderit</p>
  <div class="page-no">01</div>
</section>

<!-- 02 Technical training -->
<section class="slide slide-2">
  <svg class="abs" width="914" height="514" viewBox="0 0 914 514" aria-hidden="true">
    <path d="M0,0 H255 C350,40 400,120 379,200 C360,330 300,470 221,514 H0 Z" fill="var(--green)"/>
  </svg>
  <div class="brand-tab">
    <svg width="591" height="86" viewBox="0 0 591 86" aria-hidden="true">
      <path d="M0,0 H591 V60 C500,82 380,82 280,74 C150,64 60,40 0,0 Z" fill="var(--tab)"/>
    </svg>
    <span>HEADWEAR<br>MANUFACTURING</span>
  </div>
  <h2 class="title s2-title">TECHNICAL<br>TRAINING</h2>
  <div class="photo s2-photo" role="img" aria-label="Photo of players in batting helmets standing in a row"></div>
  <div class="copy s2-copy">
    <p>Sed ut perspiciatis unde omnis iste natus error sit voluptaaccusantium oloremquete irure dolor in reprehenderitSed ut perspiciatis unde omnis iste natus error sit voluptaaccusantium oloremquete irure dolor in reprehenderitSed ut perspiciatis unde omnis iste natus error sit voluptaaccusantium oloremquete irure dolor in reprehen</p>
    <p>Sed ut perspiciatis unde omnis iste natus error sit voluptaaccusantium oloremquete irure dolor in reprehenderitSed ut perspiciatis unde omnis iste natus error sit voluptaaccusantium</p>
  </div>
  <div class="page-no">02</div>
</section>

<!-- 03 KPI reports -->
<section class="slide slide-3">
  <div class="brand-tab">
    <svg width="591" height="86" viewBox="0 0 591 86" aria-hidden="true">
      <path d="M0,0 H591 V60 C500,82 380,82 280,74 C150,64 60,40 0,0 Z" fill="var(--tab)"/>
    </svg>
    <span>HEADWEAR<br>MANUFACTURING</span>
  </div>
  <h2 class="title s3-title">KPI REPORTS</h2>
  <div class="copy s3-copy">
    <p>Sed ut perspiciatis unde omnis iste natus error sit voluptaaccusantium oloremquete irure dolor in reprehenderitSed ut perspiciatis unde omnis iste natus error sit voluptaaccusantium oloremquete irure dolor in reprehenderitSed ut perspiciatis unde omnis iste natus error sit voluptaaccusantium oloremquete irure dolor in reprehen</p>
    <p>Sed ut perspiciatis unde omnis iste natus error sit voluptaaccusantium oloremquete irure dolor in reprehenderitSed ut perspiciatis unde omnis iste natus error sit voluptaaccusantium</p>
  </div>
  <svg class="abs s3-chart" viewBox="0 0 377 190" font-family="Montserrat, sans-serif" aria-label="Stacked bar chart">
    <g fill="#e6e5e5">
      <rect x="90" y="0" width="32" height="148"/>
      <rect x="154" y="0" width="32" height="148"/>
      <rect x="218" y="0" width="32" height="148"/>
      <rect x="282" y="0" width="32" height="148"/>
      <rect x="346" y="0" width="32" height="148"/>
    </g>
    <g font-size="6.5" fill="#333">
      <text x="0" y="15">LOREM IPSUM</text>
      <text x="0" y="46">LOREM IPSUM</text>
      <text x="0" y="77">LOREM IPSUM</text>
      <text x="0" y="108">LOREM IPSUM</text>
      <text x="0" y="139">LOREM IPSUM</text>
    </g>
    <g>
      <rect x="56" y="6" width="74" height="13" fill="var(--teal-bar)"/><rect x="130" y="6" width="102" height="13" fill="var(--tan-bar)"/>
      <rect x="56" y="37" width="90" height="13" fill="var(--teal-bar)"/><rect x="146" y="37" width="118" height="13" fill="var(--tan-bar)"/>
      <rect x="56" y="68" width="31" height="13" fill="var(--teal-bar)"/><rect x="87" y="68" width="31" height="13" fill="var(--tan-bar)"/>
      <rect x="56" y="99" width="178" height="13" fill="var(--teal-bar)"/><rect x="234" y="99" width="77" height="13" fill="var(--tan-bar)"/>
      <rect x="56" y="130" width="74" height="13" fill="var(--teal-bar)"/><rect x="130" y="130" width="143" height="13" fill="var(--tan-bar)"/>
    </g>
    <line x1="56" y1="150" x2="377" y2="150" stroke="#cfcfcf" stroke-width="0.8"/>
    <g font-size="5" fill="#555" text-anchor="middle">
      <text x="74" y="159">10</text><text x="106" y="159">20</text><text x="138" y="159">30</text>
      <text x="170" y="159">40</text><text x="202" y="159">50</text><text x="234" y="159">60</text>
      <text x="266" y="159">70</text><text x="298" y="159">80</text><text x="330" y="159">90</text>
      <text x="362" y="159">100</text>
    </g>
    <rect x="99" y="175" width="7" height="7" fill="var(--tan-bar)"/>
    <text x="111" y="181" font-size="6" fill="#333">LOREM IPSUM DOLOR SIT AMET</text>
    <rect x="238" y="175" width="7" height="7" fill="var(--teal-bar)"/>
    <text x="250" y="181" font-size="6" fill="#333">LOREM IPSUM DOLOR SIT AMET</text>
  </svg>
  <div class="page-no">03</div>
</section>

<!-- 04 Quality assurance training -->
<section class="slide slide-4">
  <div class="brand-tab">
    <svg width="591" height="86" viewBox="0 0 591 86" aria-hidden="true">
      <path d="M0,0 H591 V60 C500,82 380,82 280,74 C150,64 60,40 0,0 Z" fill="var(--tab)"/>
    </svg>
    <span>HEADWEAR<br>MANUFACTURING</span>
  </div>
  <h2 class="title s4-title">QUALITY ASSURANCE<br>TRAINING</h2>
  <p class="copy s4-copy">Sed ut perspiciatis unde omnis iste natus error sit voluptaaccusantium oloremquete irure dolor in reprehenderitSed ut perspiciatis unde omnis iste natus error sit voluptaaccusantium oloremquete irure dolor in reprehenderitSed ut perspiciatis unde omnis iste natus error sit voluptaaccusantium oloremquete irure dolor in reprehend ut perspiciatis unde omnis iste natus error sit voluptaaccusantepreheed ut perspiciatis unde omnis iste natus error sit voluptaaccusantium</p>
  <table class="qa-table">
    <thead>
      <tr>
        <th class="blank"></th>
        <th class="c-peri">Donec aliquam</th>
        <th class="c-teal">Aenean et nisl</th>
        <th class="c-blue">Pellentesque</th>
        <th class="c-cyan">Vivamus vitae</th>
        <th class="c-peri">Aenean et nisl</th>
        <th class="c-blue">Pellentesque</th>
        <th class="c-blue">Vivamus vitae</th>
        <th class="c-cyan">Consectetur</th>
      </tr>
    </thead>
    <tbody>
      <tr><th>Morbi pretium facilisis</th><td>-27,402</td><td>-42,285</td><td>-27,402</td><td>-9,146</td><td>-42,285</td><td>-27,402</td><td>-9,146</td><td>-2,459</td></tr>
      <tr><th>Curabitur elementum</th><td>$96,223</td><td>$88,306</td><td>$96,223</td><td>$105,556</td><td>$88,306</td><td>$96,223</td><td>$105,556</td><td>$133,124</td></tr>
      <tr><th>Mauris sed consequat</th><td>N/A</td><td>No</td><td>N/A</td><td>Yes</td><td>No</td><td>N/A</td><td>Yes</td><td>N/A</td></tr>
      <tr><th>Proin non accumsan</th><td>-27,402</td><td>-42,285</td><td>-27,402</td><td>-9,146</td><td>-42,285</td><td>-27,402</td><td>-9,146</td><td>-2,459</td></tr>
    </tbody>
    <tfoot>
      <tr><th>Donec accumsan:</th><td>$391,448</td><td>$422,849</td><td>$391,448</td><td>$304,864</td><td>$422,849</td><td>$391,448</td><td>$304,864</td><td>$245,995</td></tr>
    </tfoot>
  </table>
  <div class="page-no">04</div>
</section>

<!-- 05 Training reports -->
<section class="slide slide-5">
  <div class="brand-tab">
    <svg width="591" height="86" viewBox="0 0 591 86" aria-hidden="true">
      <path d="M0,0 H591 V60 C500,82 380,82 280,74 C150,64 60,40 0,0 Z" fill="var(--tab)"/>
    </svg>
    <span>HEADWEAR<br>MANUFACTURING</span>
  </div>
  <h2 class="title s5-title">TRAINING REPORTS</h2>
  <p class="copy s5-copy">Sed ut perspiciatis unde omnis iste natus error sit voluptaaccusantium oloremquete irure dolor in reprehenderitSed ut perspiciatis unde omnis iste natus error sit voluptaaccusantium oloremquete irure dolor in reprehenderit</p>
  <div class="photo s5-dash" role="img" aria-label="Screenshot of an analytics dashboard with cards, area charts and bar charts"></div>
  <div class="page-no">05</div>
</section>

<!-- 06 Thank you -->
<section class="slide slide-6">
  <div class="photo s6-photo" role="img" aria-label="Aerial photo of a domed palace and city square at dusk"></div>
  <div class="abs s6-ring"></div>
  <div class="abs s6-disc"></div>
  <div class="s6-text">
    <div class="s6-brand">HEADWEAR<br>MANUFACTURING</div>
    <div class="s6-thanks">THANK YOU</div>
    <div class="s6-contact">Call Us : +1 555 010 2040<br>info@capline-mfg.com</div>
  </div>
  <div class="page-no light">06</div>
</section>

</body>
</html>
```